Coffee Bag Label

I need a coffee bag label designed (front label and back label):
Our company "Tidy-Pod" imports organic coffee beans direct from a farm on Vorsela Mountain on a private reserve (rainforest) from Jinotega, Nicaragua.
Labels should each be 3 inches x 3 inches (with room on edges for bleed). I want the front label to catch the eye and coordinate well with the coffee bag. The bags sizes are below and pictures are attached.
Bag sizes: Lime green 12 oz bag: 3-3/8" x 2-9/16" x 10-1/4"
Black 2 oz sample stand up pouch: 4" x 6-1/2" + 2-3/8", 2oz (60g)
Black 2lb bag: 5" x 3-3/8" x 15", 2lb (1kg)
Please include as much as possible below on the front label without it looking too wordy:
1) Our logo (it's attached). Feel free to do something creative with just the bean and place "Tidy-Pod" or "Tidy-Pod Coffees" somewhere else. They don't have to be together like in the attached file. The bean can be in the background of the label as well or something else cool like in the form of a cloud over the volcano or as the sun in the sky over the volcano.
2) lime green, burnt orange, dark brown & black
3) Front label should say:
"100% Premium Arabica Nicaraguan Coffee"
"Organic, Rain Forest & Mountain Shade Grown"
Bottom of label:
"Medium Roast"
"Full body, bold flavor, nutty, hints of chocolate, with a distinct & flavorful aroma."
I want one front label file for each size bag: "2 oz" "12 oz" & "32 oz"
Back of the label:
I have uploaded a hand drawn pic of what I am thinking but if you have a better idea please submit it.
Please include as much as possible below without it looking wordy:
Directions on the perfect cup:
***2 Tbsp high quality coffee 6 Oz. cup of pure filtered water
(these can be tied into the hand-drawn picture. I will label the section each one corresponds to)
Organically Grown (sustainable)
Rainforest Grown (sustainable)
Mountain Shade Grown (sustainable)
Hand Picked (select)
Spring Water Washed (select)
Sun Dried (select)
Social Responsibility (profits help fund Bright Path Outreach Nicaragua www.brightpathoutreach.example.org)
Single Source Coffee (Single source)
Traceable Source (single source)
Website: www.Tidy-Pod.example.com
Reason: I have been asked to extend deadline by a few designers.
Thanks,
Joanne Pelter
ages 18-54
- Should have a cool border. Maybe fade from one color to another or have something more original than just a 3x3 square border.

```html
<!DOCTYPE html>
<html lang="en">
<head>
<meta charset="utf-8">
<title>Tidy-Pod Coffee Labels</title>
<link href="https://fonts.googleapis.com/css2?family=Bebas+Neue&display=swap" rel="stylesheet">
<style>
  :root {
    --page: #ffffff;
    --burnt-orange: #fb9450;
    --dark-brown: #4f2a1e;
    --lime: #a5d75a;
    --name-orange: #f6a84c;
    --sky-top: #a9c9ea;
    --sky-low: #d5e0ea;
    --mountain: #8f8378;
    --field-top: #5a7a26;
    --field-low: #2f4a1a;
    --back-top: #6e5857;
    --back-low: #4e3a2c;
  }
  * { margin: 0; padding: 0; box-sizing: border-box; }
  html, body { width: 1200px; height: 900px; overflow: hidden; background: var(--page); }
  body { position: relative; font-family: "Bebas Neue", "Arial Narrow", sans-serif; }

  .label {
    position: absolute;
    top: 228px;
    width: 464px;
    height: 463px;
    background: var(--burnt-orange);
    padding: 13px 13px 13px 14px;
  }
  .label--front { left: 98px; }
  .label--back { left: 644px; }

  .label__panel { position: relative; width: 100%; height: 100%; overflow: hidden; }

  .scene { position: absolute; inset: 0; }
  .scene--front {
    background: linear-gradient(180deg, var(--sky-top) 0%, var(--sky-low) 42%, var(--mountain) 52%, var(--field-top) 57%, var(--field-low) 100%);
  }
  .scene--back {
    background: linear-gradient(180deg, var(--back-top) 0%, var(--back-top) 45%, var(--back-low) 60%, var(--back-low) 100%);
  }

  .brand-box {
    position: absolute;
    left: 125px; top: 16px;
    width: 185px; height: 155px;
    background: var(--dark-brown);
    border-radius: 14px;
    display: flex; align-items: center; justify-content: center;
  }
  .brand-name {
    color: var(--name-orange);
    font-size: 46px;
    letter-spacing: 1px;
    line-height: 1;
  }

  .copy {
    position: absolute; left: 0; right: 0;
    text-align: center;
    color: var(--lime);
    font-size: 17px;
    line-height: 22px;
    letter-spacing: 0.2px;
  }
  .copy--origin { top: 275px; }
  .copy--roast { top: 366px; }
  .net-weight {
    position: absolute; right: 14px; top: 415px;
    color: var(--lime); font-size: 17px;
  }

  .back-brand {
    position: absolute; left: 0; right: 0; top: 55px;
    text-align: center;
    color: var(--name-orange);
    font-size: 26px; letter-spacing: 1px;
  }
  .back-rule {
    position: absolute; left: 25px; right: 23px; top: 92px;
    height: 2px; background: var(--lime);
  }
  .directions {
    position: absolute; left: 0; right: 0; top: 117px;
    text-align: center; color: var(--lime);
    font-size: 15px; line-height: 19px;
  }
  .features {
    position: absolute; left: 0; right: 0; top: 225px;
    list-style: none;
    text-align: center; color: var(--lime);
    font-size: 12.5px; line-height: 16.8px;
  }
</style>
</head>
<body>
  <section class="label label--front" aria-label="Front label">
    <div class="label__panel">
      <div class="scene scene--front" role="img" aria-label="Stylised landscape of a volcano under a cloudy sky above green coffee fields"></div>
      <div class="brand-box"><span class="brand-name">Tidy-Pod</span></div>
      <p class="copy copy--origin">100% Premium Arabica Nicaraguan Coffee<br>Organic, Rain Forest &amp; Mountain Shade Grown</p>
      <p class="copy copy--roast">Medium Roast<br>Full Body, Bold Flavor, Nutty, Hints of Chocolate<br>With a Distinct &amp; Flavorful Aroma</p>
      <span class="net-weight">12 oz.</span>
    </div>
  </section>

  <section class="label label--back" aria-label="Back label">
    <div class="label__panel">
      <div class="scene scene--back" role="img" aria-label="Darkened volcano and coffee field landscape"></div>
      <p class="back-brand">Tidy-Pod</p>
      <div class="back-rule"></div>
      <p class="directions">Directions on the perfect cup:<br>***2 Tbsp high quality coffee 6 oz. cup of pure filtered water</p>
      <ul class="features">
        <li>Organically Grown</li>
        <li>Rainforest Grown</li>
        <li>Mountain Shade Grown</li>
        <li>Hand Picked</li>
        <li>Spring Water Washed</li>
        <li>Sun Dried</li>
        <li>Growers with Social Responsibility</li>
        <li>Single Source Coffee</li>
        <li>Traceable Source</li>
      </ul>
    </div>
  </section>
</body>
</html>
```